Holvern Incorporated

Holvern is a business that provides consulting, and manages and supplies trades persons in the construction and heavy industries sector. We build, do maintenance, install machinery, and can manage projects or jobs. Would like or prefer more clean, classic designs. Blacks/greys, but open to almost anything.

Target Market(s)

Industrial/Construction/Manufacturing

Industry/Entity Type

Construction Company

Contact Information for Business Card

Clean, business name on the front, possibly have the details on the back, but open to any ideas.

Logo Text

We currently do not have a slogan, open to ideas

Font styles to use
Serif
Sans Serif

Colors

Designer to choose colors to be used in the design.

Requirements
Should not have
• the oval is not my logo, was just an idea. please don't send 20 designs with the oval

```html
<!DOCTYPE html>
<html lang="en">
<head>
<meta charset="utf-8">
<title>Holvern Incorporated — Business Card</title>
<link href="https://fonts.googleapis.com/css2?family=Lato:ital,wght@0,400;0,700;1,400&display=swap" rel="stylesheet">
<style>
  :root {
    --backdrop: #dcdcdc;
    --card: #050505;
    --ink: #f4f2ec;
    --ink-soft: #d8d5cc;
    --rule: #ffffff;
  }
  * { margin: 0; padding: 0; box-sizing: border-box; }
  html, body {
    width: 1200px; height: 787px; overflow: hidden;
    background: var(--backdrop);
    font-family: "Lato", Arial, sans-serif;
    color: var(--ink);
  }
  .sheet {
    position: relative; width: 1200px; height: 787px;
    display: flex; align-items: center; justify-content: center; gap: 40px;
  }
  .card {
    position: relative; width: 525px; height: 300px;
    background: var(--card); border-radius: 18px;
    box-shadow: 0 6px 18px rgba(0,0,0,.22);
    overflow: hidden;
  }
  .wordmark {
    display: flex; flex-direction: column; align-items: flex-end;
    font-family: "Lato", Arial, sans-serif; font-weight: 400; color: var(--ink);
  }
  .wordmark__name { font-size: 58px; letter-spacing: 1px; line-height: 1; }
  .wordmark__suffix { font-size: 9px; letter-spacing: 2.4px; margin-top: 6px; }
  .card--front { display: flex; align-items: center; justify-content: center; }
  .card--back .wordmark { position: absolute; left: 40px; top: 86px; }
  .card--back .wordmark__name { font-size: 44px; }
  .card--back .wordmark__suffix { font-size: 7px; letter-spacing: 2px; }
  .divider { position: absolute; left: 262px; top: 60px; width: 2px; height: 190px; }
  .details { position: absolute; left: 292px; top: 74px; font-size: 13px; line-height: 1.45; }
  .details__name { font-weight: 700; font-size: 15px; letter-spacing: .6px; text-transform: uppercase; }
  .details__role { font-style: italic; margin-bottom: 10px; color: var(--ink-soft); }
  .details__address { margin-bottom: 10px; }
  .contact { list-style: none; }
  .contact li { display: flex; align-items: center; gap: 8px; }
  .contact svg { width: 12px; height: 12px; flex: none; }
</style>
</head>
<body>
<main class="sheet">
  <section class="card card--front" aria-label="Card front">
    <div class="wordmark">
      <span class="wordmark__name">Holvern</span>
      <span class="wordmark__suffix">INCORPORATED</span>
    </div>
  </section>

  <section class="card card--back" aria-label="Card back">
    <div class="wordmark">
      <span class="wordmark__name">Holvern</span>
      <span class="wordmark__suffix">INCORPORATED</span>
    </div>
    <svg class="divider" viewBox="0 0 2 190" preserveAspectRatio="none" aria-hidden="true">
      <line x1="1" y1="0" x2="1" y2="190" stroke="var(--rule)" stroke-width="1.4"/>
    </svg>
    <div class="details">
      <p class="details__name">Dorian Kessler</p>
      <p class="details__role">President</p>
      <p class="details__address">1180 Granite Row, Brackwell<br>NC 4, United States</p>
      <ul class="contact">
        <li>
          <svg viewBox="0 0 12 12" aria-hidden="true"><path d="M2.5 1 L4.5 1 L5.2 3.4 L4 4.3 C4.6 5.7 6.3 7.4 7.7 8 L8.6 6.8 L11 7.5 L11 9.5 C11 10.3 10.3 11 9.5 11 C5 11 1 7 1 2.5 C1 1.7 1.7 1 2.5 1 Z" fill="var(--ink)"/></svg>
          555-014-220-318
        </li>
        <li>
          <svg viewBox="0 0 12 12" aria-hidden="true"><rect x="0.8" y="2.5" width="10.4" height="7" fill="none" stroke="var(--ink)" stroke-width="1.1"/><path d="M0.8 2.5 L6 6.6 L11.2 2.5" fill="none" stroke="var(--ink)" stroke-width="1.1"/></svg>
          office@holvernworks.com
        </li>
        <li>
          <svg viewBox="0 0 12 12" aria-hidden="true"><circle cx="6" cy="6" r="5" fill="none" stroke="var(--ink)" stroke-width="1"/><ellipse cx="6" cy="6" rx="2.2" ry="5" fill="none" stroke="var(--ink)" stroke-width="0.9"/><line x1="1" y1="6" x2="11" y2="6" stroke="var(--ink)" stroke-width="0.9"/></svg>
          www.holvernworks.com
        </li>
      </ul>
    </div>
  </section>
</main>
</body>
</html>
```